Lumora Pathway Advisory - Business card design needed

I wish to get business cards designed so that it follows my website design ... http://www.lumora-pathway.org
I need logos for QUVEX 7 and KT Summit Associate for myself which I have uploaded the files.
I wish my qualifications PhD PMP FAICD to be smaller print than my name.
Regards
Leopold
Industry/Entity Type
Business
Contact Information for Business Card
Lumora Pathway Advisory
Dr Leopold Marsh PhD PMP FAICD
Director
PO Box 418 Kelvendale NSW 2093 AUSTRALIA
T:+61 2 9352 6710 M:+61 437 918000 F: +61 2 9368 2000
Email: leopold.marsh@lumora-pathway.org
Website: http://www.lumora-pathway.org

```html
<!DOCTYPE html>
<html lang="en">
<head>
<meta charset="utf-8">
<title>Lumora Pathway Advisory – Business Card</title>
<link rel="stylesheet" href="https://fonts.googleapis.com/css2?family=Lato:ital,wght@0,400;0,700;1,400&display=swap">
<style>
  :root {
    --page-bg: #5d6272;
    --card-top: #3b4861;
    --card-bottom: #313c52;
    --name-glow: #4a5876;
    --rule: rgba(255, 255, 255, 0.14);
    --text: #ffffff;
    --text-soft: #e9edf3;
    --band: #dcdde0;
    --badge-light: #ffffff;
    --badge-blue: #1b9bd7;
  }
  * { box-sizing: border-box; margin: 0; padding: 0; }
  html, body { width: 1200px; height: 944px; overflow: hidden; }
  body {
    background: var(--page-bg);
    font-family: "Lato", Arial, sans-serif;
    color: var(--text);
    position: relative;
  }
  .card {
    position: absolute;
    left: 338px; top: 52px;
    width: 524px; height: 836px;
    background: linear-gradient(180deg, var(--card-top) 0%, var(--card-bottom) 100%);
    box-shadow: 0 6px 18px rgba(0, 0, 0, 0.45);
    overflow: hidden;
  }
  .brand {
    position: absolute; left: 0; top: 0; width: 100%; height: 252px;
    text-align: center;
  }
  .brand-name {
    position: absolute; left: 0; top: 65px; width: 100%;
    font-weight: 700; font-size: 42px; line-height: 55px;
  }
  .brand-url {
    position: absolute; left: 0; top: 186px; width: 100%;
    font-weight: 700; font-size: 22px;
    color: var(--text-soft);
  }
  .person {
    position: absolute; left: 0; top: 252px; width: 100%; height: 129px;
    border-top: 1px solid var(--rule);
    border-bottom: 1px solid var(--rule);
    background: radial-gradient(ellipse at 45% 40%, var(--name-glow) 0%, rgba(74, 88, 118, 0) 70%);
  }
  .person-block { position: absolute; left: 131px; top: 10px; }
  .person-name { font-size: 32px; line-height: 40px; }
  .person-quals { font-style: italic; font-size: 24px; line-height: 32px; margin-left: 2px; }
  .person-role { font-size: 24px; line-height: 30px; margin-left: 2px; }
  .email {
    position: absolute; left: 0; top: 404px; width: 100%;
    text-align: center; font-size: 24px; color: var(--text-soft);
  }
  .partner-band {
    position: absolute; left: 0; top: 459px; width: 100%; height: 125px;
    background: var(--band);
  }
  .partner-band svg { display: block; }
  .address {
    position: absolute; left: 0; top: 601px; width: 100%;
    text-align: center; font-size: 24px; line-height: 43px;
  }
  .contacts {
    position: absolute; left: 125px; top: 692px;
    font-size: 24px; line-height: 33px;
    border-collapse: collapse;
  }
  .contacts td { padding: 0; }
  .contacts .label { width: 30px; text-align: center; }
  .contacts .sep { width: 38px; text-align: center; }
</style>
</head>
<body>
  <main class="card">
    <header class="brand">
      <h1 class="brand-name">Lumora<br>Pathway Advisory</h1>
      <p class="brand-url">www.lumora-pathway.org</p>
    </header>

    <section class="person">
      <div class="person-block">
        <h2 class="person-name" style="font-weight:400">Dr Leopold Marsh</h2>
        <p class="person-quals">PhD PMP FAICD</p>
        <p class="person-role">Director</p>
      </div>
    </section>

    <p class="email">leopold.marsh@lumora-pathway.org</p>

    <section class="partner-band">
      <svg width="524" height="125" viewBox="0 0 524 125">
        <rect class="badge-certificate" x="21" y="19" width="247" height="86" fill="var(--badge-light)" role="img" aria-label="QUVEX 7 certification badge"/>
        <rect class="badge-partner" x="282" y="24" width="220" height="78" fill="var(--badge-blue)" role="img" aria-label="KT Summit Associate partner badge"/>
      </svg>
    </section>

    <address class="address" style="font-style:normal">
      PO Box : 418,Kelvendale<br>NSW 2093, AUSTRALIA
    </address>

    <table class="contacts">
      <tr><td class="label">T</td><td class="sep">:</td><td>+61 2 9352 6710</td></tr>
      <tr><td class="label">M</td><td class="sep">:</td><td>+61 437 918000</td></tr>
      <tr><td class="label">F</td><td class="sep">:</td><td>+61 2 9368 2000</td></tr>
    </table>
  </main>
</body>
</html>
```